Design a Brochure for Brackenmoor Group

Brackenmoor Group, consists of 3 divisions, Brackenmoor Property Investments, Brackenmoor Private Wealth and Brackenmoor Home Loans. Each with their own colour combination (see the attached brochures)

we need to get a more suitable corporate brochure designed, taking a look at the actual look of the brochure as well as the content. I have uploaded a short version and long version of the brochure. They will need to run side by side. The A3 folded, will be generally handed out whilst the longer version is only for serious clients, as the cost of producing is too great to just randomly distribute.

experience in the property investment and financial industry, would be a huge advantage.

```html
<!DOCTYPE html>
<html lang="en">
<head>
<meta charset="utf-8">
<title>Brackenmoor Group – Brochure</title>
<link rel="stylesheet" href="https://fonts.googleapis.com/css2?family=Source+Sans+3:wght@300;400;600&display=swap">
<style>
  :root {
    --band-grey: #5e5e5e;
    --page-white: #ffffff;
    --body-ink: #231f20;
    --logo-grey: #5a5a5a;
    --accent-green: #8dc63f;
    --panel-blue: #6a82d3;
    --headline-blue: #1f7fc3;
    --square-green: #1fa34a;
  }
  * { margin: 0; padding: 0; box-sizing: border-box; }
  html, body { width: 848px; height: 1200px; overflow: hidden; background: var(--page-white); }
  .brochure-page {
    position: relative;
    width: 848px;
    height: 1200px;
    overflow: hidden;
    background: var(--page-white);
    font-family: "Source Sans 3", "Myriad Pro", sans-serif;
    color: var(--body-ink);
  }
  .top-band {
    position: absolute; left: 0; top: 0;
    width: 100%; height: 91px;
    background: var(--band-grey);
  }
  .brand-lockup {
    position: absolute; left: 79px; top: 222px;
  }
  .brand-name {
    display: flex; align-items: center; gap: 8px;
    font-weight: 300;
    font-size: 55px;
    line-height: 52px;
    letter-spacing: 0.5px;
    color: var(--logo-grey);
  }
  .brand-square {
    width: 30px; height: 30px;
    background: var(--square-green);
  }
  .division-line {
    margin-top: 6px;
    font-weight: 300;
    font-size: 13px;
    letter-spacing: 0.3px;
    color: var(--logo-grey);
  }
  .division-line .divider { font-weight: 600; margin: 0 5px; color: var(--body-ink); }
  .intro-column {
    position: absolute; top: 303px;
    width: 336px;
    font-size: 10.6px;
    line-height: 13.4px;
    text-align: justify;
    hyphens: auto;
  }
  .intro-column p + p { margin-top: 13.4px; }
  .intro-column.left { left: 79px; }
  .intro-column.right { left: 434px; width: 343px; }
  .feature-mosaic {
    position: absolute; left: 0; top: 479px;
    width: 848px; height: 495px;
  }
  .headline {
    position: absolute; left: 73px; top: 990px;
    font-weight: 400;
    font-size: 34px;
    letter-spacing: -0.3px;
    color: var(--headline-blue);
  }
  .bottom-band {
    position: absolute; left: 0; bottom: 0;
    width: 100%; height: 49px;
    background: var(--band-grey);
    display: flex; align-items: center;
    padding-left: 45px;
    color: var(--page-white);
    font-size: 16px;
    letter-spacing: 0.3px;
  }
</style>
</head>
<body>
<main class="brochure-page">
  <div class="top-band"></div>

  <header class="brand-lockup">
    <div class="brand-name"><span class="brand-square"></span>BRACKENMOOR</div>
    <div class="division-line">Home Loans<span class="divider">|</span>Property Investments<span class="divider">|</span>Private Wealth</div>
  </header>

  <section class="intro-column left">
    <p>At Brackenmoor we have one priority and that is to ensure that nothing is ever left to chance. Now you might be asking, “What do they mean by this?” Let us explain… It’s quite simple really… Elias Whitcombe put it best when he said “By failing to prepare, you are preparing to fail.”</p>
    <p>We truly believe that everyone has the power within themselves to achieve Financial security and increased wealth however sometimes just lack the guidance and tools to get the job done. With our experience in wealth development, property investment and finance, we can assist YOU in achieving your goals.</p>
  </section>

  <section class="intro-column right">
    <p>Our Financial solutions are carefully selected to better serve your individual needs. Unlike many others, we involve you in the formulation of your success plan. Making sure that it is a plan that you can adhere to and not rebel against. We would like you to Join the movement in income enhancement and achieve better success with Brackenmoor who will guide you every step of the way. By registering with us on this website, you can start your journey to a better future, a better lifestyle and a new way of thinking.</p>
  </section>

  <svg class="feature-mosaic" viewBox="0 0 848 495" xmlns="http://www.w3.org/2000/svg">
    <defs>
      <linearGradient id="sea-tone" x1="0" y1="0" x2="0" y2="1">
        <stop offset="0" stop-color="#e4e9ec"/>
        <stop offset="0.5" stop-color="#aab7bf"/>
        <stop offset="1" stop-color="#4e6470"/>
      </linearGradient>
      <linearGradient id="fairway-tone" x1="0" y1="0" x2="0" y2="1">
        <stop offset="0" stop-color="#a9cbe8"/>
        <stop offset="0.55" stop-color="#9cbf7a"/>
        <stop offset="1" stop-color="#5fa332"/>
      </linearGradient>
      <linearGradient id="villa-tone" x1="0" y1="0" x2="0" y2="1">
        <stop offset="0" stop-color="#3b6f7f"/>
        <stop offset="0.45" stop-color="#a0765a"/>
        <stop offset="1" stop-color="#2b5f78"/>
      </linearGradient>
    </defs>
    <g stroke="var(--accent-green)" stroke-width="2.5" stroke-linejoin="round">
      <path class="panel-blue-tall" fill="var(--panel-blue)"
            d="M103,2 H170 Q195,2 201,25 L244,232 Q247,246 244,260 L204,468 Q199,491 175,491 H103 Q73,491 73,461 V32 Q73,2 103,2 Z"/>
      <path class="photo-yacht" fill="url(#sea-tone)" role="img" aria-label="Photo of a luxury motor yacht cruising at sea"
            d="M254,2 H565 Q598,2 586,30 L448,214 Q436,233 412,233 H302 Q284,233 276,216 L227,110 Q224,103 224,94 V32 Q224,2 254,2 Z"/>
      <path class="photo-golf" fill="url(#fairway-tone)" role="img" aria-label="Photo of a couple walking a golf course carrying golf bags"
            d="M292,258 H424 Q444,258 449,278 L460,460 Q462,491 432,491 H254 Q224,491 226,460 L268,278 Q273,258 292,258 Z"/>
      <path class="panel-blue-short" fill="var(--panel-blue)"
            d="M514,172 Q530,156 546,172 L624,455 Q631,491 595,491 H486 Q456,491 456,461 V264 Q456,250 465,239 Z"/>
      <path class="photo-villa" fill="url(#villa-tone)" role="img" aria-label="Photo of a modern villa with a pool at dusk"
            d="M682,2 H747 Q777,2 777,32 V461 Q777,491 747,491 H690 Q666,491 660,468 L579,140 Q576,127 584,117 L660,13 Q668,2 682,2 Z"/>
    </g>
  </svg>

  <h1 class="headline">Building a brighter future, today...</h1>

  <footer class="bottom-band">BRACKENMOOR | 2013</footer>
</main>
</body>
</html>
```